Simple but elegant business card/logo design for exclusive beauty business

We need a logo designed for a new elegant and exclusive beauty business called "R". The logo itself should be a stylistic and custom design for the letter "R". We would like the business card to have the logo as the centrepiece on a clean background. Gold Logo on black background or silver on white background.

The business card details should be displayed centre of the card. Details are as follows:

Tamsin Earle
Facebook: /shinesoftlyr
Instagram: /shinesoftlyr

The words "Shine Softly" should also appear somewhere on the card.

Industry/Entity Type

Business

Logo Text

G

Requirements
Must have
• Design must be simple, clean and elegant
Should not have
• The design should not be cluttered

```html
<!DOCTYPE html>
<html lang="en">
<head>
<meta charset="utf-8">
<title>R — Business Card</title>
<link rel="stylesheet" href="https://fonts.googleapis.com/css2?family=Montserrat:wght@300;400;500&display=swap">
<style>
  :root {
    --backdrop: #1e1e1f;
    --card: #262627;
    --card-edge: #303031;
    --gold: #c08a3e;
    --ink-light: #e9e9e9;
  }
  * { margin: 0; padding: 0; box-sizing: border-box; }
  html, body { width: 1200px; height: 1200px; overflow: hidden; background: var(--backdrop); }
  .canvas {
    position: relative;
    width: 1200px;
    height: 1200px;
    font-family: "Montserrat", sans-serif;
  }
  .card {
    position: absolute;
    width: 560px;
    height: 320px;
    background: var(--card);
    border: 1px solid var(--card-edge);
    box-shadow: 0 18px 40px rgba(0,0,0,0.45);
  }
  .card-front { left: 90px; top: 150px; display: flex; align-items: center; justify-content: center; }
  .brand-name {
    color: var(--gold);
    font-weight: 400;
    font-size: 120px;
    line-height: 1;
  }
  .card-back {
    left: 550px; top: 540px;
    display: flex; flex-direction: column; align-items: center; justify-content: center;
    color: var(--ink-light);
  }
  .tagline { font-size: 15px; letter-spacing: 2px; font-weight: 400; margin-bottom: 14px; }
  .holder-name { font-size: 30px; letter-spacing: 3px; font-weight: 500; margin-bottom: 34px; }
  .socials { display: flex; gap: 60px; }
  .social { display: flex; align-items: center; gap: 10px; font-size: 17px; font-weight: 300; letter-spacing: 1px; }
  .social-mark { width: 18px; height: 18px; border: 1.5px solid var(--gold); border-radius: 4px; }
  .brand-large {
    position: absolute;
    left: 800px; top: 920px;
    color: var(--gold);
    font-weight: 400;
    font-size: 200px;
    line-height: 1;
  }
</style>
</head>
<body>
  <main class="canvas">
    <section class="card card-front" aria-label="Card front">
      <span class="brand-name">R</span>
    </section>

    <section class="card card-back" aria-label="Card back">
      <p class="tagline">"Shine Softly"</p>
      <h1 class="holder-name">Tamsin Earle</h1>
      <div class="socials">
        <span class="social"><span class="social-mark"></span>/shinesoftlyr</span>
        <span class="social"><span class="social-mark"></span>/shinesoftlyr</span>
      </div>
    </section>

    <span class="brand-large">R</span>
  </main>
</body>
</html>
```